2022 Merel Quandry High Roof Extended Cab

I want a 3/4 side wrap, (rear of front doors back) and complete back of van, Photo background using either of the photos below, Dark Blue logo’s

Target Market(s)

Marine industry

Industry/Entity Type

Marine

Colors
0054AA
0677BA
7BADD7
CADEEF
E8F1F8

Requirements
Must have
• Educational content

```html
<!DOCTYPE html>
<html lang="en">
<head>
<meta charset="utf-8">
<title>Quaybrisk Dock Fenders – Merel Quandry Van Wrap</title>
<link href="https://fonts.googleapis.com/css2?family=Montserrat:wght@400;500;600&display=swap" rel="stylesheet">
<style>
  :root {
    --navy: #0a2a8c;
    --brand-blue: #0054AA;
    --mid-blue: #0677BA;
    --sky: #7BADD7;
    --pale: #CADEEF;
    --mist: #E8F1F8;
    --body-white: #f4f5f7;
    --trim: #2a2b2e;
    --glass: #3a3d44;
    --stage: #d2d3d6;
    --tail: #c9302c;
  }
  * { margin: 0; padding: 0; box-sizing: border-box; }
  html, body { width: 1200px; height: 2700px; overflow: hidden; background: var(--stage); }
  .wrap-sheet { width: 1200px; height: 2700px; display: flex; flex-direction: column; }
  .view { width: 1200px; height: 675px; display: block; flex: none; }
  text { font-family: "Montserrat", sans-serif; }
  .headline { font-weight: 500; fill: #fff; }
  .benefit { font-weight: 400; fill: #fff; }
  .phone { font-weight: 500; fill: #fff; }
  .brand-name { font-weight: 600; fill: var(--navy); }
  .body-panel { fill: var(--body-white); }
  .trim { fill: var(--trim); }
  .glass { fill: var(--glass); }
  .tyre { fill: #1e1f21; }
  .hub { fill: #c4c7cc; }
  .swoosh { fill: var(--navy); }
  .pill { fill: var(--navy); }
  .tick-mark { stroke: #fff; fill: none; stroke-linecap: round; stroke-linejoin: round; }
</style>
</head>
<body>
<main class="wrap-sheet">

  <!-- Front view -->
  <svg class="view view-front" viewBox="0 0 1200 675" aria-label="Front of van">
    <path class="body-panel" d="M385,45 Q585,30 800,45 L820,300 Q835,360 825,470 L345,470 Q335,360 350,300 Z"/>
    <text class="brand-name" x="585" y="112" font-size="34" text-anchor="middle">Quaybrisk</text>
    <rect class="trim" x="380" y="152" width="410" height="26"/>
    <text class="headline" x="585" y="172" font-size="20" text-anchor="middle">QUAYBRISK DOCK FENDERS</text>
    <path class="glass" d="M380,178 L790,178 L782,300 Q585,312 388,300 Z"/>
    <rect class="trim" x="288" y="255" width="55" height="80" rx="10"/>
    <rect class="trim" x="830" y="255" width="55" height="80" rx="10"/>
    <rect class="trim" x="450" y="385" width="270" height="110" rx="18"/>
    <rect class="trim" x="335" y="470" width="500" height="115" rx="20"/>
    <rect fill="var(--mist)" x="520" y="505" width="130" height="28"/>
    <rect class="tyre" x="340" y="560" width="70" height="75" rx="12"/>
    <rect class="tyre" x="765" y="560" width="70" height="75" rx="12"/>
  </svg>

  <!-- Left side view -->
  <svg class="view view-left" viewBox="0 0 1200 675" aria-label="Left side of van">
    <defs>
      <clipPath id="left-body"><path d="M45,460 L48,385 Q55,345 95,330 L180,290 L410,130 Q450,100 520,100 L1110,100 Q1145,104 1150,145 L1155,460 Z"/></clipPath>
      <linearGradient id="marina-left" x1="0" y1="0" x2="0" y2="1">
        <stop offset="0" stop-color="#9cc3e6"/>
        <stop offset=".4" stop-color="#e3edf5"/>
        <stop offset=".55" stop-color="#5f8fba"/>
        <stop offset="1" stop-color="#1f4f86"/>
      </linearGradient>
    </defs>
    <g clip-path="url(#left-body)">
      <rect class="body-panel" x="0" y="0" width="1200" height="480"/>
      <path fill="var(--brand-blue)" d="M795,90 L1160,90 L1160,460 L500,460 Q700,360 760,250 Q790,190 795,150 Z"/>
      <path fill="url(#marina-left)" role="img" aria-label="Marina photo with moored yachts along a dock" d="M640,400 Q715,340 752,331 L1160,331 L1160,460 L500,460 Z"/>
      <path class="swoosh" d="M490,460 Q700,360 750,250 L768,256 Q730,380 570,460 Z"/>
      <rect class="trim" x="0" y="457" width="1200" height="60"/>
    </g>
    <rect class="trim" x="40" y="457" width="1120" height="60" rx="8"/>
    <path class="glass" d="M272,300 L350,215 L450,205 L450,362 L262,362 Z"/>
    <rect class="pill" x="506" y="142" width="573" height="36" rx="18"/>
    <text class="headline" x="792" y="172" font-size="31" text-anchor="middle">CUSTOM MADE DOCK FENDERS</text>
    <g font-size="19">
      <g transform="translate(815,197)"><circle r="8" class="swoosh"/><path class="tick-mark" d="M-4,0 L-1,3 L4,-3" stroke-width="2"/></g>
      <text class="benefit" x="831" y="204">Boat Protection</text>
      <g transform="translate(815,220)"><circle r="8" class="swoosh"/><path class="tick-mark" d="M-4,0 L-1,3 L4,-3" stroke-width="2"/></g>
      <text class="benefit" x="831" y="227">American Manufacture</text>
      <g transform="translate(815,243)"><circle r="8" class="swoosh"/><path class="tick-mark" d="M-4,0 L-1,3 L4,-3" stroke-width="2"/></g>
      <text class="benefit" x="831" y="250">Five Year Warnty</text>
      <g transform="translate(815,266)"><circle r="8" class="swoosh"/><path class="tick-mark" d="M-4,0 L-1,3 L4,-3" stroke-width="2"/></g>
      <text class="benefit" x="831" y="273">Closed Cell Foam Core</text>
    </g>
    <path d="M810,294 q-6,4 0,16 q6,10 14,12 l4,-5 l-6,-5 l-3,3 q-5,-3 -7,-9 l3,-3 l-3,-6 Z" fill="#fff"/>
    <text class="phone" x="834" y="319" font-size="29">1855 204 6190</text>
    <text class="brand-name" x="372" y="420" font-size="30" text-anchor="middle">Quaybrisk</text>
    <circle class="tyre" cx="226" cy="530" r="64"/><circle class="hub" cx="226" cy="530" r="36"/>
    <circle class="tyre" cx="944" cy="530" r="64"/><circle class="hub" cx="944" cy="530" r="36"/>
  </svg>

  <!-- Rear view -->
  <svg class="view view-rear" viewBox="0 0 1200 675" aria-label="Rear of van">
    <defs>
      <clipPath id="rear-body"><rect x="341" y="65" width="510" height="460" rx="26"/></clipPath>
      <linearGradient id="marina-rear" x1="0" y1="0" x2="0" y2="1">
        <stop offset="0" stop-color="#6f9fd0"/>
        <stop offset=".55" stop-color="#e3edf5"/>
        <stop offset=".75" stop-color="#5f8fba"/>
        <stop offset="1" stop-color="#1f4f86"/>
      </linearGradient>
    </defs>
    <g clip-path="url(#rear-body)">
      <rect class="body-panel" x="330" y="50" width="530" height="480"/>
      <path fill="var(--brand-blue)" d="M330,50 L860,50 L860,380 Q595,330 330,375 Z"/>
      <path fill="url(#marina-rear)" role="img" aria-label="Marina photo with a motor yacht beside the dock" d="M378,138 L812,138 L812,338 Q595,322 378,350 Z"/>
      <path class="swoosh" d="M330,360 Q595,318 860,364 L860,380 Q595,336 330,378 Z"/>
      <line x1="595" y1="65" x2="595" y2="525" stroke="#9a9da3" stroke-width="2"/>
    </g>
    <rect fill="var(--tail)" x="535" y="70" width="120" height="10" rx="5"/>
    <rect class="pill" x="398" y="95" width="393" height="30" rx="15"/>
    <text class="headline" x="594" y="118" font-size="22" text-anchor="middle">QUAYBRISK DOCK FENDERS</text>
    <g font-size="25">
      <g transform="translate(440,173)"><circle r="11" class="swoosh"/><path class="tick-mark" d="M-5,0 L-1,4 L5,-4" stroke-width="2.4"/></g>
      <text class="benefit" x="462" y="182">Boat Protection</text>
      <g transform="translate(440,205)"><circle r="11" class="swoosh"/><path class="tick-mark" d="M-5,0 L-1,4 L5,-4" stroke-width="2.4"/></g>
      <text class="benefit" x="462" y="214">American Manufacture</text>
      <g transform="translate(440,236)"><circle r="11" class="swoosh"/><path class="tick-mark" d="M-5,0 L-1,4 L5,-4" stroke-width="2.4"/></g>
      <text class="benefit" x="462" y="245">Five Year Warnty</text>
      <g transform="translate(440,268)"><circle r="11" class="swoosh"/><path class="tick-mark" d="M-5,0 L-1,4 L5,-4" stroke-width="2.4"/></g>
      <text class="benefit" x="462" y="277">Closed Cell Foam Core</text>
    </g>
    <text class="brand-name" x="490" y="441" font-size="30" text-anchor="middle">Quaybrisk</text>
    <rect class="trim" x="628" y="400" width="56" height="12" rx="6"/>
    <path class="swoosh" d="M490,479 L715,479 L700,510 L476,510 Z"/>
    <path d="M508,483 q-5,3 0,13 q5,8 11,10 l3,-4 l-5,-4 l-2,2 q-4,-2 -6,-7 l2,-2 l-2,-5 Z" fill="#fff"/>
    <text class="phone" x="528" y="503" font-size="22">1855 204 6190</text>
    <rect fill="var(--tail)" x="340" y="348" width="24" height="167" rx="6"/>
    <rect fill="var(--tail)" x="828" y="348" width="24" height="167" rx="6"/>
    <rect class="trim" x="334" y="515" width="524" height="95" rx="14"/>
    <rect fill="var(--mist)" x="650" y="542" width="105" height="26"/>
    <rect class="tyre" x="360" y="595" width="70" height="30" rx="8"/>
    <rect class="tyre" x="762" y="595" width="70" height="30" rx="8"/>
  </svg>

  <!-- Right side view -->
  <svg class="view view-right" viewBox="0 0 1200 675" aria-label="Right side of van">
    <defs>
      <clipPath id="right-body"><path transform="translate(1200,0) scale(-1,1)" d="M45,460 L48,385 Q55,345 95,330 L180,290 L410,130 Q450,100 520,100 L1110,100 Q1145,104 1150,145 L1155,460 Z"/></clipPath>
      <linearGradient id="marina-right" x1="0" y1="0" x2="0" y2="1">
        <stop offset="0" stop-color="#9cc3e6"/>
        <stop offset=".4" stop-color="#e3edf5"/>
        <stop offset=".55" stop-color="#5f8fba"/>
        <stop offset="1" stop-color="#1f4f86"/>
      </linearGradient>
    </defs>
    <g clip-path="url(#right-body)">
      <rect class="body-panel" x="0" y="0" width="1200" height="480"/>
      <g transform="translate(1200,0) scale(-1,1)">
        <path fill="var(--brand-blue)" d="M795,90 L1160,90 L1160,460 L500,460 Q700,360 760,250 Q790,190 795,150 Z"/>
        <path fill="url(#marina-right)" role="img" aria-label="Marina photo with moored yachts along a dock" d="M640,400 Q715,340 752,331 L1160,331 L1160,460 L500,460 Z"/>
        <path class="swoosh" d="M490,460 Q700,360 750,250 L768,256 Q730,380 570,460 Z"/>
      </g>
    </g>
    <rect class="trim" x="40" y="457" width="1120" height="60" rx="8"/>
    <path class="glass" transform="translate(1200,0) scale(-1,1)" d="M272,300 L350,215 L450,205 L450,362 L262,362 Z"/>
    <rect class="pill" x="121" y="142" width="573" height="36" rx="18"/>
    <text class="headline" x="408" y="172" font-size="31" text-anchor="middle">CUSTOM MADE DOCK FENDERS</text>
    <g font-size="19">
      <g transform="translate(157,197)"><circle r="8" class="swoosh"/><path class="tick-mark" d="M-4,0 L-1,3 L4,-3" stroke-width="2"/></g>
      <text class="benefit" x="173" y="204">Boat Protection</text>
      <g transform="translate(157,220)"><circle r="8" class="swoosh"/><path class="tick-mark" d="M-4,0 L-1,3 L4,-3" stroke-width="2"/></g>
      <text class="benefit" x="173" y="227">American Manufacture</text>
      <g transform="translate(157,243)"><circle r="8" class="swoosh"/><path class="tick-mark" d="M-4,0 L-1,3 L4,-3" stroke-width="2"/></g>
      <text class="benefit" x="173" y="250">Five Year Warnty</text>
      <g transform="translate(157,266)"><circle r="8" class="swoosh"/><path class="tick-mark" d="M-4,0 L-1,3 L4,-3" stroke-width="2"/></g>
      <text class="benefit" x="173" y="273">Closed Cell Foam Core</text>
    </g>
    <path d="M164,294 q-6,4 0,16 q6,10 14,12 l4,-5 l-6,-5 l-3,3 q-5,-3 -7,-9 l3,-3 l-3,-6 Z" fill="#fff"/>
    <text class="phone" x="188" y="319" font-size="29">1855 204 6190</text>
    <text class="brand-name" x="828" y="425" font-size="30" text-anchor="middle">Quaybrisk</text>
    <circle class="tyre" cx="256" cy="530" r="64"/><circle class="hub" cx="256" cy="530" r="36"/>
    <circle class="tyre" cx="974" cy="530" r="64"/><circle class="hub" cx="974" cy="530" r="36"/>
  </svg>

</main>
</body>
</html>
```